Manufacturing company needs new business card.

I need a unique Business Card that will truly stand out. Nothing too busy. Simple is good, right? Not looking for a standard design either. No cookie cutter layout. I am just looking for something interesting and a bit different. Does't have to completely off the wall crazy, just not your run of the mill business card. Clean and modern with a touch of industrial.

Target Market(s)

Air conditioning industry, Architects, builders.

Industry/Entity Type

Business

Contact Information for Business Card

Details to be included on card are:

Peter Vance
Managing Director

T: 1300 847 519
M: 0428 593 174
W: www.brenvaleworks.com.au
E: peter.vance@brenvaleworks.com.au
A: 58 Harwick Lane, Sydney NSW 2000

Font styles to use
Sans Serif

Colors
0355a3
848484
fbfbfb

Requirements
Must have
• Card design must be landscape.

```html
<!DOCTYPE html>
<html lang="en">
<head>
<meta charset="utf-8">
<title>Brenvale Works – Business Card</title>
<link rel="stylesheet" href="https://fonts.googleapis.com/css2?family=Arimo:wght@400;700&display=swap">
<style>
  :root {
    --brand-blue: #0355a3;
    --deep-blue: #1d3f8f;
    --steel-grey: #848484;
    --rule-grey: #9a9a9a;
    --paper: #fbfbfb;
    --ink: #2b2b2b;
    --stage: #2a2a2a;
  }
  * { margin: 0; padding: 0; box-sizing: border-box; }
  html, body {
    width: 1200px; height: 997px; overflow: hidden;
    background: var(--stage);
    font-family: "Arimo", Arial, sans-serif;
  }
  .sheet {
    width: 1200px; height: 997px;
    display: flex; flex-direction: column; align-items: center; justify-content: center;
    gap: 60px;
  }
  .card {
    position: relative;
    width: 620px; height: 378px;
    border-radius: 4px;
    overflow: hidden;
  }
  /* Back */
  .card--back { background: var(--brand-blue); }
  .back-brand {
    position: absolute; left: 0; right: 0; top: 160px;
    display: flex; align-items: center; justify-content: center; gap: 14px;
  }
  .brand-square { width: 22px; height: 22px; }
  .card--back .brand-square { background: var(--paper); }
  .back-brand .brand-name { color: var(--paper); font-size: 32px; font-weight: 400; }

  /* Front */
  .card--front { background: var(--paper); }
  .front-brand {
    position: absolute; left: 60px; top: 95px;
    display: flex; align-items: center; gap: 14px;
  }
  .card--front .brand-square { background: var(--brand-blue); width: 26px; height: 26px; }
  .front-brand .brand-name { color: var(--brand-blue); font-size: 34px; font-weight: 400; }
  .rule { position: absolute; height: 2px; background: var(--rule-grey); }
  .rule--brand { left: 230px; top: 165px; width: 360px; }
  .rule--name { left: 200px; top: 232px; width: 180px; }

  .address {
    position: absolute; right: 32px; top: 186px;
    text-align: right; font-size: 15px; line-height: 19px; color: var(--steel-grey);
  }
  .address .company { font-weight: 700; color: #5c5c5c; }
  .address .street, .address .state { color: var(--brand-blue); }

  .person { position: absolute; left: 36px; top: 218px; }
  .person-name { font-size: 19px; font-weight: 700; color: var(--deep-blue); }
  .person-role { font-size: 14px; color: var(--steel-grey); margin-top: 2px; }

  .contacts { position: absolute; left: 36px; top: 266px; list-style: none; }
  .contact {
    display: flex; align-items: center; gap: 10px;
    height: 24px; font-size: 16px; color: var(--brand-blue);
  }
  .contact-icon { width: 16px; height: 16px; flex: none; }

  .band { position: absolute; left: 0; bottom: 0; width: 620px; height: 378px; }
  .web {
    position: absolute; right: 26px; top: 314px;
    font-size: 14px; color: var(--paper);
  }
</style>
</head>
<body>
<main class="sheet">
  <section class="card card--back" aria-label="Card back">
    <div class="back-brand">
      <span class="brand-square"></span>
      <span class="brand-name">Brenvale Works</span>
    </div>
  </section>

  <section class="card card--front" aria-label="Card front">
    <svg class="band" viewBox="0 0 620 378" aria-hidden="true">
      <path d="M0 348 L330 348 Q350 348 356 340 L420 340 L420 352 L0 360 Z" fill="#8a8a8a"/>
      <path d="M0 364 L370 358 Q410 354 420 330 Q428 300 460 300 L620 300 L620 378 L0 378 Z" fill="#0355a3"/>
    </svg>

    <div class="front-brand">
      <span class="brand-square"></span>
      <span class="brand-name">Brenvale Works</span>
    </div>
    <div class="rule rule--brand"></div>

    <address class="address" style="font-style:normal">
      <div class="company">Brenvale Works</div>
      <div class="street">58 Harwick Lane, Sydney</div>
      <div class="state">NSW 2000</div>
    </address>

    <div class="person">
      <div class="person-name">Peter Vance</div>
      <div class="person-role">Managing Director</div>
    </div>
    <div class="rule rule--name"></div>

    <ul class="contacts">
      <li class="contact">
        <svg class="contact-icon" viewBox="0 0 16 16" aria-hidden="true"><circle cx="8" cy="8" r="8" fill="#0355a3"/><rect x="4" y="6" width="8" height="5" rx="1" fill="#fbfbfb"/><rect x="5" y="4.5" width="6" height="2" rx="1" fill="#fbfbfb"/></svg>
        <span>1300 847 519</span>
      </li>
      <li class="contact">
        <svg class="contact-icon" viewBox="0 0 16 16" aria-hidden="true"><circle cx="8" cy="8" r="8" fill="#0355a3"/><rect x="5.5" y="3.5" width="5" height="9" rx="1" fill="#fbfbfb"/></svg>
        <span>0428 593 174</span>
      </li>
      <li class="contact">
        <svg class="contact-icon" viewBox="0 0 16 16" aria-hidden="true"><circle cx="8" cy="8" r="8" fill="#0355a3"/><rect x="4" y="5" width="8" height="6" fill="#fbfbfb"/><path d="M4 5 L8 8.5 L12 5" fill="none" stroke="#0355a3" stroke-width="1"/></svg>
        <span>peter.vance@brenvaleworks.com.au</span>
      </li>
    </ul>

    <div class="web">www.brenvaleworks.com.au</div>
  </section>
</main>
</body>
</html>
```